Fun & Healthy Dog Treat Business Needs a Business & Loyalty Card

We need a business card design for a business that provides healthy dog products.

The design should communicate a healthy aspect and should communicate that the business focuses on healthy produce.

We would like some aspects if not all of our current logo to appear on the card.

We would also like a two sided card with the back of the card being able to be used as a loyalty program where after purchasing 7 items the buyer receives a free gift. There should be a way of identifying how many purchases a customer has made and if possible enable at least 4 - 5 gives be able to be given on one card. ie make 7 purchases and receive a give, to be able to be done 4 - 5 times before they need to be given a new card.

Rather than the focus be solely on dog treats we would like the card's focus to be a bit wider should we decide to enter other markets in the future and therefore not mention dog treats.

We want the card to be colourful while still retaining a very healthy aspect.

We also need the card to have pictures such as a dog or dogs head that enable us to determine how many items a customer has purchase before we give them a free gift.

Please see our website for further details regarding our business including contact details. www.marlowsbowl.com.au

Target Market(s)

Dog lovers who are health concious

Industry/Entity Type

Pet

Contact Information for Business Card

Products for Healthy Dogs
Web Address - www.marlowsbowl.com.au
Email address - info@marlowsbowl.com.au

Font styles to use
Serif

Colors
acd037
f04a50

Requirements
Must have
• Marlow's Larder
• Products for Healthy Dogs
• Web Address - www.marlowsbowl.com.au
• Email address - info@marlowsbowl.com.au
• Mobile Number - 0417 358 619
Nice to have
• Part of our current logo
• Blend in with current logo but not include the words healthy dog treats
• The flip side of the card should have a Loyalty Program where when you purchase 7 products you receive a free gift.
Should not have
• Should not include the words healthy dog treats
• Should not have the fixed line phone number

```html
<!DOCTYPE html>
<html lang="en">
<head>
<meta charset="utf-8">
<title>Marlow's Larder – Business Card</title>
<link rel="stylesheet" href="https://fonts.googleapis.com/css2?family=Arimo:wght@400;700&display=swap">
<style>
  :root {
    --page: #ffffff;
    --band: #a8241f;
    --band-fade: #e9b9b5;
    --brand-red: #c4161c;
    --ink: #1e1e1e;
    --title-ink: #2b2b2b;
    --cut-line: #7a7a7a;
    --card-edge: #8c8c8c;
    --photo-light: #fbfaf7;
    --photo-mid: #e6dfd2;
    --photo-deep: #c9b89c;
    --mascot-tone: #b9804f;
  }
  html, body {
    margin: 0;
    padding: 0;
    width: 1200px;
    height: 350px;
    overflow: hidden;
    background: var(--page);
  }
  .sheet {
    position: relative;
    width: 1200px;
    height: 350px;
    font-family: "Arimo", Arial, sans-serif;
  }
  .card {
    position: absolute;
    top: 13px;
    height: 310px;
  }
  .card--front { left: 29px; width: 551px; }
  .card--back  { left: 636px; width: 545px; }
  .card svg { display: block; overflow: visible; }
  .band { fill: var(--band); }
  .card-edge { fill: none; stroke: var(--card-edge); stroke-width: 2; }
  .cut-guide { fill: none; stroke: var(--cut-line); stroke-width: 1.5; stroke-dasharray: 7 4; }
  .scissors { fill: none; stroke: #333; stroke-width: 1.6; }
  .front-name { font-size: 26px; font-weight: 700; fill: var(--title-ink); }
  .tagline { font-size: 22px; font-weight: 700; fill: var(--brand-red); }
  .contact { font-size: 20px; fill: var(--ink); }
  .back-name { font-size: 34px; font-weight: 700; fill: var(--brand-red); }
  .back-tagline { font-size: 18px; fill: var(--ink); }
</style>
</head>
<body>
<main class="sheet">

  <section class="card card--front">
    <svg width="551" height="310" viewBox="0 0 551 310">
      <defs>
        <linearGradient id="front-photo" x1="0" y1="0" x2="0" y2="1">
          <stop offset="0" stop-color="var(--band-fade)"/>
          <stop offset="0.08" stop-color="var(--photo-light)"/>
          <stop offset="0.45" stop-color="var(--photo-light)"/>
          <stop offset="0.75" stop-color="var(--photo-mid)"/>
          <stop offset="1" stop-color="var(--photo-deep)"/>
        </linearGradient>
      </defs>
      <rect class="photo" x="0" y="82" width="551" height="228" fill="url(#front-photo)" role="img" aria-label="Soft photograph of a basket of sliced wholegrain bread on a checked napkin"/>
      <rect class="band" x="0" y="11" width="551" height="71"/>
      <rect class="mascot" x="17" y="168" width="160" height="128" rx="36" fill="var(--mascot-tone)" opacity="0.5" role="img" aria-label="Cartoon dog mascot wearing a chef's hat"/>
      <text class="front-name" x="16" y="53">Marlow's Larder</text>
      <text class="tagline" x="291" y="103" text-anchor="middle">Products for Healthy Dogs</text>
      <text class="contact" x="16" y="134">Web Address - www.marlowsbowl.com.au</text>
      <text class="contact" x="16" y="158">Email address - info@marlowsbowl.com.au</text>
      <text class="contact" x="522" y="291" text-anchor="end">Mobile Number - 0417 358 619</text>
      <rect class="cut-guide" x="11" y="11" width="529" height="288"/>
      <path class="card-edge" d="M551 0 V310 H0"/>
      <g class="scissors" transform="translate(8 -10)">
        <circle cx="4" cy="14" r="3.5"/>
        <circle cx="13" cy="14" r="3.5"/>
        <path d="M6 11 L18 0 M11 11 L-1 0"/>
      </g>
    </svg>
  </section>

  <section class="card card--back">
    <svg width="545" height="310" viewBox="0 0 545 310">
      <defs>
        <linearGradient id="back-photo" x1="0" y1="0" x2="0" y2="1">
          <stop offset="0" stop-color="var(--band-fade)"/>
          <stop offset="0.1" stop-color="var(--photo-light)"/>
          <stop offset="0.3" stop-color="var(--photo-light)"/>
          <stop offset="0.6" stop-color="var(--photo-mid)"/>
          <stop offset="1" stop-color="var(--photo-deep)"/>
        </linearGradient>
      </defs>
      <rect class="photo" x="0" y="90" width="545" height="220" fill="url(#back-photo)" role="img" aria-label="Soft photograph of a basket of sliced wholegrain bread on a checked napkin"/>
      <rect class="band" x="0" y="11" width="545" height="79"/>
      <text class="back-name" x="275" y="115" text-anchor="middle">Marlow's Larder</text>
      <text class="back-tagline" x="275" y="136" text-anchor="middle">Products for Healthy Dogs</text>
      <rect class="cut-guide" x="11" y="11" width="523" height="288"/>
      <path class="card-edge" d="M545 0 V310 H0"/>
      <g class="scissors" transform="translate(8 -10)">
        <circle cx="4" cy="14" r="3.5"/>
        <circle cx="13" cy="14" r="3.5"/>
        <path d="M6 11 L18 0 M11 11 L-1 0"/>
      </g>
    </svg>
  </section>

</main>
</body>
</html>
```